Womans Supplement Designs

Launching a Supplement company and need to get some initial designs created, I've attached our logo and the bottle type that I want the samples done one.

This project is for our Whey Protein we are starting with Vanilla, chocolate and strawberry banana

(ALL DESIGN VARIATIONS MUST BE A WHITE BOTTLE NOT BLACK)

(FOR DESIGN SAMPLES PLEASE USE THE SUPPLEMENT BOTTLE STYLE I PROVIDED)

Whoever is selected the winner I will have more work for you to complete the disigns for the rest of the products in the line, Just want to get this shake completed first

Women

• Must have our current logo involved

the name of this product will be "BLUE OAK"

Must have this slogan,

ALL-IN-ONE PREMIUM PROTEIN NUTRITIONAL SHAKE FOR BLACK WOMEN

This is our meal replacement

the design should try to keep the same look and feel of the existing provided supplement images

we are starting with chocolate, vanilla and strawberry banana

this is for women and should look colorful and appeal to them
• Do not use an image of a person or lady, don't want it branded to a person

```html
<!DOCTYPE html>
<html lang="en">
<head>
<meta charset="utf-8">
<title>Blue Oak Whey Protein Labels</title>
<link rel="stylesheet" href="https://fonts.googleapis.com/css2?family=Archivo+Black&family=Michroma&family=Poppins:ital,wght@0,400;0,700;0,800;1,700;1,800&display=swap">
<style>
  :root {
    --ink: #000000;
    --paper: #ffffff;
    --pink: #ef47a0;
    --shadow: #3a1a2a;
    --panel-grey: #c9c9c9;
    --chocolate: #c4552b;
    --strawberry: #c32a0d;
    --vanilla: #e8900f;
  }
  html, body {
    margin: 0;
    padding: 0;
    width: 1200px;
    height: 3127px;
    overflow: hidden;
    background: var(--paper);
  }
  .sheet {
    position: relative;
    width: 1200px;
    height: 3127px;
  }
  .label {
    position: absolute;
    left: 0;
    width: 1200px;
    height: 919.5px;
    display: block;
  }
  .label--chocolate { top: 37.7px; --band: var(--chocolate); }
  .label--strawberry { top: 1084.6px; --band: var(--strawberry); }
  .label--vanilla { top: 2139px; --band: var(--vanilla); }

  .base { fill: var(--ink); }
  .w-frame { fill: var(--paper); }
  .top-glow { fill: url(#topGlow); }
  .stripe { fill: url(#stripeFade); }
  .sheen { fill: url(#sheenFade); }
  .flavor-band { fill: var(--band); }
  .flavor-panel { fill: var(--panel-grey); }

  .brand-mark { fill: var(--ink); }
  .brand-name {
    font-family: "Michroma", sans-serif;
    font-size: 27px;
    fill: var(--ink);
    letter-spacing: 3px;
  }
  .product-name {
    font-family: "Archivo Black", sans-serif;
    font-size: 118px;
    fill: var(--pink);
    stroke: var(--paper);
    stroke-width: 5px;
    paint-order: stroke;
  }
  .product-name-shadow {
    font-family: "Archivo Black", sans-serif;
    font-size: 118px;
    fill: var(--shadow);
  }
  .tagline {
    font-family: "Poppins", sans-serif;
    font-weight: 800;
    font-style: italic;
    font-size: 24px;
    fill: var(--paper);
  }
  .tagline-box { fill: var(--paper); }
  .tagline--boxed { fill: var(--ink); }
  .protein-type {
    font-family: "Poppins", sans-serif;
    font-weight: 800;
    font-size: 25px;
    fill: var(--paper);
  }
  .net-weight {
    font-family: "Poppins", sans-serif;
    font-weight: 400;
    font-size: 35px;
    fill: var(--paper);
  }
  .band-slogan {
    font-family: "Poppins", sans-serif;
    font-weight: 800;
    font-style: italic;
    font-size: 37px;
    fill: var(--paper);
  }
  .flavor-name {
    font-family: "Poppins", sans-serif;
    font-weight: 800;
    fill: var(--band);
  }
</style>
</head>
<body>
<svg width="0" height="0" style="position:absolute" aria-hidden="true">
  <defs>
    <linearGradient id="topGlow" x1="0" y1="0" x2="0" y2="1" gradientUnits="objectBoundingBox">
      <stop offset="0" stop-color="#ffffff"/>
      <stop offset="0.55" stop-color="#f2f2f2"/>
      <stop offset="1" stop-color="#000000"/>
    </linearGradient>
    <linearGradient id="stripeFade" x1="0" y1="0" x2="1" y2="1" gradientUnits="objectBoundingBox">
      <stop offset="0" stop-color="#ffffff"/>
      <stop offset="0.4" stop-color="#cfcfcf"/>
      <stop offset="1" stop-color="#000000"/>
    </linearGradient>
    <linearGradient id="sheenFade" x1="1" y1="0" x2="0" y2="1" gradientUnits="objectBoundingBox">
      <stop offset="0" stop-color="#000000"/>
      <stop offset="0.45" stop-color="#bdbdbd"/>
      <stop offset="0.7" stop-color="#ffffff"/>
      <stop offset="1" stop-color="#9a9a9a"/>
    </linearGradient>
    <linearGradient id="chocolateSplash" x1="0" y1="0" x2="0" y2="1">
      <stop offset="0" stop-color="#8a4a34"/>
      <stop offset="1" stop-color="#3f1c10"/>
    </linearGradient>
    <linearGradient id="strawberrySplash" x1="0" y1="0" x2="0" y2="1">
      <stop offset="0" stop-color="#f6c9cf"/>
      <stop offset="0.6" stop-color="#f3b3bc"/>
      <stop offset="1" stop-color="#f7e3b0"/>
    </linearGradient>
    <linearGradient id="vanillaSplash" x1="0" y1="0" x2="0" y2="1">
      <stop offset="0" stop-color="#fbf3c4"/>
      <stop offset="1" stop-color="#efe0a0"/>
    </linearGradient>

    <g id="labelArtwork">
      <rect class="base" x="0" y="0" width="988" height="757"/>
      <polygon class="top-glow" points="268,0 720,0 606,320 382,320"/>
      <polygon class="stripe" points="0,55 0,100 250,367 250,322"/>
      <polygon class="stripe" points="0,140 0,180 300,501 300,461"/>
      <polygon class="stripe" points="0,350 0,395 340,759 340,714"/>
      <polygon class="stripe" points="0,440 0,480 290,790 290,750"/>
      <polygon class="stripe" points="0,530 0,570 220,805 220,765"/>
      <polygon class="stripe" points="0,620 0,655 140,805 140,770"/>
      <polygon class="w-frame" points="0,215 418,662 470,606 497,649 520,606 570,662 570,757 418,757 0,300"/>
      <polygon class="base" points="400,757 497,655 590,757"/>
      <polygon class="sheen" points="570,662 988,55 988,175 570,757"/>
      <polygon class="flavor-band" points="570,757 988,175 988,270 652,757"/>
      <polygon class="flavor-panel" points="988,270 988,757 652,757"/>
    </g>

    <g id="labelText">
      <circle class="brand-mark" cx="494" cy="98" r="34"/>
      <text class="brand-name" x="494" y="180" text-anchor="middle">NOVA GRACE</text>
      <text class="product-name-shadow" x="503" y="420" text-anchor="middle" textLength="520" lengthAdjust="spacingAndGlyphs">BLUE OAK</text>
      <text class="product-name" x="499" y="415" text-anchor="middle" textLength="520" lengthAdjust="spacingAndGlyphs">BLUE OAK</text>
      <text class="tagline" x="494" y="457" text-anchor="middle">ALL-IN-ONE PREMIUM PROTEIN</text>
      <text class="tagline" x="494" y="486" text-anchor="middle">NUTRITIONAL SHAKE</text>
      <rect class="tagline-box" x="365" y="492" width="258" height="28"/>
      <text class="tagline tagline--boxed" x="494" y="514" text-anchor="middle">FOR BLACK WOMEN</text>
      <text class="protein-type" x="490" y="592" text-anchor="middle">WHEY PROTEIN</text>
      <text class="net-weight" x="494" y="737" text-anchor="middle">750g</text>
      <text class="band-slogan" x="0" y="0" text-anchor="middle" transform="translate(805 490) rotate(-54.8)">THIS IS OUR MEAL REPLACEMENT</text>
    </g>
  </defs>
</svg>

<main class="sheet">
  <svg class="label label--chocolate" viewBox="0 0 988 757" role="group" aria-label="Chocolate whey protein label">
    <use href="#labelArtwork"/>
    <path role="img" aria-label="Chocolate shake pouring with chocolate pieces and splash" fill="url(#chocolateSplash)"
          d="M800 500 C 820 560, 840 620, 830 670 C 780 690, 720 710, 700 757 L 988 757 L 988 690 C 940 680, 900 670, 870 660 C 860 610, 830 540, 800 500 Z"/>
    <use href="#labelText"/>
    <text class="flavor-name" font-size="44" x="0" y="0" text-anchor="middle" transform="translate(974 503) rotate(-90)">Chocolate</text>
  </svg>

  <svg class="label label--strawberry" viewBox="0 0 988 757" role="group" aria-label="Strawberry banana whey protein label">
    <use href="#labelArtwork"/>
    <path role="img" aria-label="Strawberry milk splash with banana slices and a strawberry" fill="url(#strawberrySplash)"
          d="M815 510 C 830 560, 820 610, 790 650 C 760 670, 745 710, 750 745 C 820 757, 900 757, 930 740 C 935 700, 920 650, 900 630 C 880 580, 850 540, 815 510 Z"/>
    <use href="#labelText"/>
    <text class="flavor-name" font-size="33" x="0" y="0" text-anchor="middle" transform="translate(970 517) rotate(-90)">Strawberry banana</text>
  </svg>

  <svg class="label label--vanilla" viewBox="0 0 988 757" role="group" aria-label="Vanilla whey protein label">
    <use href="#labelArtwork"/>
    <path role="img" aria-label="Vanilla shake splash with vanilla pods and flower" fill="url(#vanillaSplash)"
          d="M820 500 C 835 550, 830 600, 790 640 C 760 660, 720 700, 720 740 C 800 757, 900 752, 930 730 C 935 690, 920 650, 880 630 C 865 580, 845 530, 820 500 Z"/>
    <use href="#labelText"/>
    <text class="flavor-name" font-size="44" x="0" y="0" text-anchor="middle" transform="translate(974 519) rotate(-90)">Vanilla</text>
  </svg>
</main>
</body>
</html>
```